Referral Card thats different from the rest

Business card size-

Referral card that will be given to clients, in turn they will pass it on to their friends.

The referee will add their name and address, and friends name to card before it is passed on

Referee gets 2 FREE movie tickets

Friend gets $25 OFF their service

Company is an electrical contracting company specialising in the domestic market.

I would like the card to be fun not so serious!
Completely open minded to any and every creative idea!

attached is 2 photo of an example of what another business has, i am trying to achieve something similiar
Updates

I have increased the budget, ;)

i have added 2 x photos of what i am trying to achieve. this is from another business, I am after something similar to this
Thanks

I have updated the design brief.
this should help make it easir and more clear
Thanks

Target Market(s)

Home owners from 30yrs +

Industry/Entity Type

Electrical

Requirements
Must have
• Logo - Not a main feature of card
1300 846 572 on both sides
Lic no: 418695D (doesn’t have to be big) prefer on back

The main feature of the front of the card is the 2 free movie tickets for Referee & $25 OFF Friends first bill

HOW ABOUT TWO FREE MOVIE TICKETS?
It is easy! Know someone who needs an electrician? Maybe a friend, family member, relative or work colleague.
Tell them about us, and we will take $25 off their first bill and give you two FREE Movie Tickets just for introducing us.
To make a referral fill out this card and give it to your friend.

Recommended By:____________
Address:__________________
Frinds name: _____________

*this offer is only valued for work over $55. Non transferable for cash. This coupon is limited to 1 per customer, not to be used in conjunction with any other offer
Nice to have
• Catchy heading on card
example- tell a friend for cash card, (if i was giving away cash vouchers..)

example- keep me in your wallet and pass me on

```html
<!DOCTYPE html>
<html lang="en">
<head>
<meta charset="utf-8">
<title>Refer a Friend – Bright Spark Electrical</title>
<link rel="stylesheet" href="https://fonts.googleapis.com/css2?family=Bangers&family=Oswald:wght@300;400&display=swap">
<style>
  :root{
    --yellow:#fff27a;
    --yellow-pale:#fff59b;
    --ink:#1a1a1a;
    --red:#c8262b;
    --orange:#ec6a24;
    --green:#3c9a3a;
    --sky:#a9d6ee;
    --white:#ffffff;
    --contact:#3f8f31;
  }
  *{box-sizing:border-box;margin:0;padding:0}
  html,body{width:1200px;height:343px;overflow:hidden;background:var(--white)}
  .card{position:relative;width:1200px;height:343px;font-family:"Oswald",sans-serif;color:var(--ink)}

  /* front / left side */
  .front{position:absolute;left:0;top:0;width:600px;height:343px;background:var(--yellow);overflow:hidden}
  .stripes{position:absolute;left:0;top:0}
  .headline{position:absolute;right:26px;top:30px;text-align:right;font-family:"Bangers",cursive;font-style:italic;
    font-size:42px;line-height:52px;letter-spacing:2px;color:var(--ink)}
  .perks{position:absolute;left:28px;top:160px;list-style:none}
  .perks li{display:flex;align-items:center;gap:14px;height:58px;font-size:23px;font-weight:400}
  .perks svg{flex:none}
  .contact{position:absolute;left:82px;top:286px;font-size:15px;color:var(--contact);letter-spacing:.3px}
  .contact .sep{margin:0 12px}
  .mascot{position:absolute;left:470px;top:182px;width:92px;height:118px;border-radius:46px 46px 20px 20px;
    background:linear-gradient(160deg,#cfe4f2 0%,#f2b15a 45%,#3a9a3c 100%)}
  .brand{position:absolute;left:420px;top:296px;width:110px;font-family:"Oswald",sans-serif;font-weight:400;
    font-size:14px;line-height:16px;color:var(--orange);text-transform:uppercase;text-align:center}

  /* back / right side */
  .back{position:absolute;left:600px;top:0;width:600px;height:343px;background:var(--white)}
  .band{position:absolute}
  .band--top{left:0;top:0;width:600px;height:12px;background:var(--red)}
  .band--left{left:0;top:0;width:10px;height:343px;background:var(--orange)}
  .band--right{right:0;top:0;width:12px;height:343px;background:var(--sky)}
  .band--bottom{left:0;bottom:0;width:600px;height:12px;background:var(--green)}
  .panel{position:absolute;left:20px;top:24px;width:566px;height:306px;background:var(--yellow-pale);padding:10px 18px 0}
  .panel h2{font-family:"Bangers",cursive;font-style:italic;font-weight:400;font-size:28px;letter-spacing:1.5px;line-height:34px}
  .intro{margin-top:6px;text-align:center;font-weight:300;font-size:16.5px;line-height:29px}
  .fields{margin-top:8px;list-style:none}
  .fields li{display:flex;align-items:flex-end;height:29px;font-size:16.5px;font-weight:300}
  .fields li::after{content:"";flex:1;border-bottom:1.5px solid var(--ink);margin-left:2px;margin-bottom:5px}
  .fine{margin-top:10px;font-size:10.5px;line-height:17px;font-weight:300;width:526px}
  .phone{position:absolute;right:22px;bottom:6px;font-family:"Bangers",cursive;font-style:italic;font-size:21px;letter-spacing:1.5px}
</style>
</head>
<body>
<main class="card">
  <section class="front">
    <svg class="stripes" width="600" height="343" viewBox="0 0 600 343" aria-hidden="true">
      <polygon points="0,0 120,0 0,44" fill="var(--white)"/>
      <polygon points="120,0 160,0 0,59 0,44" fill="var(--red)"/>
      <polygon points="160,0 200,0 0,74 0,59" fill="var(--orange)"/>
      <polygon points="200,0 240,0 0,89 0,74" fill="var(--green)"/>
      <polygon points="240,0 280,0 0,104 0,89" fill="var(--sky)"/>
    </svg>
    <h1 class="headline">Refer a friend<br>and you both win!</h1>
    <ul class="perks">
      <li>
        <svg width="30" height="30" viewBox="0 0 30 30" aria-hidden="true">
          <circle cx="15" cy="15" r="13" fill="none" stroke="var(--orange)" stroke-width="3"/>
          <polygon points="17,6 9,16 14,16 12,24 21,13 16,13" fill="var(--red)"/>
        </svg>
        You get 2 FREE movie tickets
      </li>
      <li>
        <svg width="30" height="30" viewBox="0 0 30 30" aria-hidden="true">
          <circle cx="15" cy="15" r="13" fill="none" stroke="var(--orange)" stroke-width="3"/>
          <polygon points="17,6 9,16 14,16 12,24 21,13 16,13" fill="var(--red)"/>
        </svg>
        Your friend gets $25 OFF their service
      </li>
    </ul>
    <p class="contact">1300 846 572<span class="sep">|</span>www.brightsparkelectrical.com.au</p>
    <div class="mascot" role="img" aria-label="Cartoon electrician superhero mascot holding a light bulb"></div>
    <p class="brand">Bright Spark Electrical</p>
  </section>

  <section class="back">
    <div class="band band--top"></div>
    <div class="band band--left"></div>
    <div class="band band--right"></div>
    <div class="band band--bottom"></div>
    <div class="panel">
      <h2>How about those movie tickets?</h2>
      <p class="intro">It’s easy! Know someone who needs an electrician? Maybe a friend, family member or colleague? Tell them about us, and we’ll take $25 off their first bill and give you 2 FREE Movie Tickets just for introducing us.*</p>
      <ul class="fields">
        <li>Friend’s name:</li>
        <li>Address:</li>
        <li>Recommended by:</li>
      </ul>
      <p class="fine">*This offer is only valued for work over $55. Non transferable for cash. This coupon is limited to 1 per customer, not to be used in conjunction with any other offer. Lic no: 418695D</p>
      <p class="phone">1300 846 572</p>
    </div>
  </section>
</main>
</body>
</html>
```